professional business card

A Clean looking business card for a money transfer company. Our company is call Pavolex= Transfer + Send = Transcend (next level)
to show professionalism as well as some effects to show digital tech.

1 side to have position, name and address
2 side to have company name and show that we provide money exchange and cross-border money transfer

Target Market(s)

Remittance companies and high net worth individuals

Industry/Entity Type

Finance

Contact Information for Business Card

Name, address, email, title, services- money exchange and cross-border remittance

Requirements
Nice to have
• Digital age feel

```html
<!DOCTYPE html>
<html lang="en">
<head>
<meta charset="UTF-8">
<title>Pavolex Business Card</title>
<link href="https://fonts.googleapis.com/css2?family=Montserrat:ital,wght@0,300;0,400;0,600;1,400&display=swap" rel="stylesheet">
<style>
  :root {
    --navy: #283643;
    --cyan: #6fccdc;
    --mist: #e0e0e0;
    --ink: #3a3a3a;
    --paper: #ffffff;
  }
  html, body {
    margin: 0;
    padding: 0;
    width: 969px;
    height: 1200px;
    overflow: hidden;
    background: var(--paper);
  }
  .card-sheet {
    display: block;
    width: 969px;
    height: 1200px;
    font-family: "Montserrat", sans-serif;
  }
  .fill-navy { fill: var(--navy); }
  .fill-cyan { fill: var(--cyan); }
  .fill-mist { fill: var(--mist); }
  .fill-paper { fill: var(--paper); }
  .icon-line { fill: none; stroke: var(--ink); stroke-width: 2.4; stroke-linecap: round; stroke-linejoin: round; }
  .icon-person { fill: none; stroke: var(--cyan); stroke-width: 3.5; }
  .rule { stroke: var(--ink); stroke-width: 2; }
  .brand-name { fill: var(--paper); font-weight: 600; font-size: 54px; letter-spacing: 1px; }
  .holder-name { font-weight: 300; font-size: 32px; letter-spacing: 1px; fill: var(--ink); }
  .holder-name .accent { fill: var(--cyan); }
  .holder-position { font-style: italic; font-size: 16px; letter-spacing: 1px; fill: var(--ink); }
  .contact-text { font-size: 20px; font-weight: 400; letter-spacing: 1.6px; fill: var(--ink); }
  .website { font-style: italic; font-size: 26px; letter-spacing: 3px; fill: var(--ink); }
</style>
</head>
<body>
<svg class="card-sheet" viewBox="0 0 1050 1300" xmlns="http://www.w3.org/2000/svg">
  <defs>
    <clipPath id="back-card-shape">
      <rect x="0" y="703" width="1050" height="597" rx="60" ry="60"/>
    </clipPath>
  </defs>

  <!-- Front card -->
  <g class="card-front">
    <path class="fill-mist" d="M500 0 L532 0 C552 90 532 180 494 265 C480 380 525 500 630 597 L430 597 Z"/>
    <path class="fill-cyan" d="M486 268 C474 390 508 490 604 597 L420 597 Z"/>
    <path class="fill-navy" d="M60 0 L520 0 C540 90 520 180 486 268 C432 380 412 480 425 597 L60 597 Q0 597 0 537 L0 60 Q0 0 60 0 Z"/>

    <g class="brand-lockup">
      <circle class="fill-cyan" cx="250" cy="115" r="24"/>
      <text class="brand-name" x="250" y="202" text-anchor="middle">PAVOLEX</text>
    </g>

    <g class="name-plate">
      <path class="fill-mist" d="M676 77 L1035 77 L1050 92 L1050 183 L676 183 A53 53 0 0 1 676 77 Z"/>
      <g class="icon-person">
        <circle cx="665" cy="124" r="9"/>
        <path d="M648 153 L648 146 A17 12 0 0 1 682 146 L682 153 Z"/>
      </g>
      <text class="holder-name" x="708" y="135"><tspan class="accent">YOUR</tspan> NAME</text>
      <text class="holder-position" x="710" y="157">POSITION</text>
      <line class="rule" x1="810" y1="151" x2="1004" y2="151"/>
    </g>

    <g class="contact-phone">
      <path class="icon-line" d="M650 273 Q644 276 646 284 Q654 300 672 306 Q678 307 680 300 L672 293 L666 296 Q658 291 654 283 L657 277 Z"/>
      <path class="icon-line" d="M664 273 Q676 276 679 288"/>
      <text class="contact-text" x="716" y="275">+000 2103 8894</text>
      <text class="contact-text" x="716" y="303">+000 8899 2376</text>
      <line class="rule" x1="716" y1="311" x2="1050" y2="311"/>
    </g>

    <g class="contact-web">
      <circle class="icon-line" cx="662" cy="381" r="18"/>
      <ellipse class="icon-line" cx="662" cy="381" rx="8" ry="18"/>
      <line class="icon-line" x1="644" y1="375" x2="680" y2="375"/>
      <line class="icon-line" x1="644" y1="387" x2="680" y2="387"/>
      <line class="icon-line" x1="662" y1="363" x2="662" y2="399"/>
      <text class="contact-text" x="717" y="366">www.yourcompany.com</text>
      <text class="contact-text" x="717" y="394">info@yourmail.com</text>
      <line class="rule" x1="716" y1="405" x2="1050" y2="405"/>
    </g>

    <g class="contact-address">
      <path class="icon-line" d="M663 486 C652 474 650 468 650 463 A13 13 0 0 1 676 463 C676 468 674 474 663 486 Z"/>
      <circle class="icon-line" cx="663" cy="463" r="4"/>
      <ellipse class="icon-line" cx="663" cy="486" rx="17" ry="5"/>
      <text class="contact-text" x="716" y="464">Your Address Here</text>
      <text class="contact-text" x="716" y="492">001234</text>
      <line class="rule" x1="716" y1="505" x2="1050" y2="505"/>
    </g>
  </g>

  <!-- Back card -->
  <g class="card-back" clip-path="url(#back-card-shape)">
    <rect class="fill-navy" x="0" y="703" width="1050" height="597"/>
    <rect class="fill-cyan" x="0" y="1155" width="1050" height="18"/>
    <rect class="fill-paper" x="0" y="1173" width="1050" height="97"/>
    <path class="fill-paper" d="M0 1270 L40 1270 Q10 1275 0 1300 Z M1050 1270 L1010 1270 Q1040 1275 1050 1300 Z"/>
  </g>
  <g class="back-lockup">
    <circle class="fill-cyan" cx="525" cy="916" r="28"/>
    <text class="brand-name" x="525" y="1003" text-anchor="middle">PAVOLEX</text>
  </g>
  <text class="website" x="514" y="1231" text-anchor="middle">www.yourwebsite.com</text>
</svg>
</body>
</html>
```